Ridgecrest Balusters Website Redesign

I want a fresh new design for my website. Original website
www.ridgecrestbalusters.example. Will need to add additional photos for winning designer. Please use the basic layout for new design. Looking to get a more modern, functional site to attract new customer and ne bale to highlight past projects. Need it to be easy to navigate and get in touch with me for inquiries.

Target Market(s)

Builders and home owners in WA state

Industry/Entity Type

Building, Construction, Deck building

Coding

Coded - Design and coding required

Number of Pages Required

5+ page

Font styles to use
Sans Serif

Colors
0054AA
0677BA
7BADD7
CADEEF
E8F1F8
0094D4
00A9DD
6FCCEA
C7EBF8
E9F6FB
00AB8E
00BBA5
67D7C9
C6EFE9
E9F9F6
59FF00
82FF00
B8FF75
E3FFCB
F4FFEA

Requirements
Must have
• Will need to add more photos of completed projects
Nice to have
• Fresh take on old website, something modern
Should not have
• Nothing comes to mind

```html
<!DOCTYPE html>
<html lang="en">
<head>
<meta charset="utf-8">
<title>Ridgecrest Balusters</title>
<link href="https://fonts.googleapis.com/css2?family=Poppins:wght@400;500;600;700;800&display=swap" rel="stylesheet">
<style>
:root{
  --green:#0b6b30;
  --green-dark:#0a4d23;
  --green-deep:#063a1a;
  --ink:#111;
  --text:#333;
  --muted:#555;
  --light:#f2f2f2;
  --line:#d8d8d8;
  --white:#fff;
}
*{box-sizing:border-box;margin:0;padding:0}
html,body{width:1200px;height:4644px;overflow:hidden}
body{font-family:'Poppins',sans-serif;color:var(--text);background:var(--white);position:relative}
.abs{position:absolute}
.topbar{left:0;top:0;width:1200px;height:45px;background:var(--green-dark);color:var(--white);font-size:11px;font-weight:500}
.topbar span{position:absolute;top:15px}
.social-dot{position:absolute;top:12px;width:22px;height:22px;border-radius:50%;background:var(--white)}
.nav{left:0;top:45px;width:1200px;height:65px;background:var(--white)}
.brand{position:absolute;left:63px;top:20px;font-size:19px;font-weight:700;color:var(--green);display:flex;align-items:center;gap:8px}
.brand i{display:block;width:14px;height:14px;background:var(--green)}
.nav a{position:absolute;top:24px;font-size:15px;font-weight:600;color:var(--ink);text-decoration:none}
.btn-contact{position:absolute;left:1004px;top:11px;width:136px;height:43px;background:#000;color:#fff;font-size:14px;font-weight:600;display:flex;align-items:center;justify-content:center}
.hero{left:0;top:110px;width:1200px;height:820px}
.hero-label{left:61px;top:274px;width:285px;height:56px;background:#d9d9d9;color:#222;font-size:22px;font-weight:600;display:flex;align-items:center;justify-content:center}
.hero h1{left:61px;top:338px;width:760px;font-size:55px;line-height:68px;font-weight:800;color:var(--white)}
.hero-text{left:61px;top:494px;width:690px;font-size:13.5px;line-height:20px;color:#eee}
.btn{background:var(--green);color:var(--white);font-weight:600;display:flex;align-items:center;justify-content:center}
.ph{position:absolute}
.about-title{left:627px;top:1072px;font-size:46px;font-weight:800;color:var(--ink)}
.about-sub{left:627px;top:1134px;width:470px;font-size:22px;line-height:27px;font-weight:600;color:var(--ink)}
.about-para{left:627px;top:1202px;width:340px;font-size:14px;line-height:22px}
.check{position:absolute;left:627px;font-size:13.5px;display:flex;align-items:center;gap:10px}
.check b{width:18px;height:18px;border-radius:50%;background:var(--green);display:flex;align-items:center;justify-content:center}
.badge{left:65px;top:1389px;width:236px;height:81px;background:var(--green);color:#fff;font-size:22px;font-weight:700;line-height:26px;text-align:center;display:flex;flex-direction:column;justify-content:center}
.band{left:0;width:1200px;background:radial-gradient(ellipse at 50% 40%,#127a3a,var(--green-deep) 85%)}
.sec-title{left:0;width:1200px;text-align:center;font-size:46px;font-weight:800}
.sec-sub{left:0;width:1200px;text-align:center;font-size:22px;font-weight:600}
.svc{position:absolute;top:1742px;width:258px;height:321px;background:#fff}
.svc .ph{left:0;top:0;width:258px;height:175px}
.svc h3{position:absolute;left:15px;top:194px;font-size:18px;line-height:21px;font-weight:700;color:var(--ink)}
.svc p{position:absolute;left:15px;top:246px;width:230px;font-size:13.5px;line-height:21px;color:#444}
.svc .arrow{position:absolute;right:0;bottom:0;width:36px;height:20px;background:#111}
.discover{left:521px;top:2108px;width:162px;height:43px;background:#fff;color:#111;font-size:14px;font-weight:600;display:flex;align-items:center;justify-content:center}
.post{position:absolute;top:2396px;width:352px;height:454px;background:#fff;box-shadow:0 0 8px rgba(0,0,0,.18)}
.post .ph{left:16px;top:16px;width:320px;height:211px}
.post h3{position:absolute;left:16px;top:260px;font-size:19px;line-height:22px;font-weight:600;color:var(--ink)}
.post .ex{position:absolute;left:16px;top:312px;width:320px;font-size:14px;line-height:22px}
.post hr{position:absolute;left:0;top:358px;width:352px;border:0;border-top:2px solid #888}
.post .author{position:absolute;left:16px;top:380px;display:flex;align-items:center;gap:12px;font-size:14px;font-weight:600;color:var(--ink)}
.post .author i{width:36px;height:36px;border-radius:50%;background:#c9c9c9}
.post .note{position:absolute;left:16px;top:426px;font-size:11.5px}
.info-ic{position:absolute;left:77px;width:76px;height:76px;border-radius:50%;background:var(--green);display:flex;align-items:center;justify-content:center}
.info-h{position:absolute;left:166px;font-size:19px;font-weight:600;color:var(--ink)}
.info-t{position:absolute;left:166px;font-size:14px;line-height:21px;width:290px}
.field{position:absolute;background:#fff;box-shadow:0 0 6px rgba(0,0,0,.18);font-size:14px;font-weight:500;color:#222;padding:20px 22px}
.footer a{position:absolute;top:4522px;font-size:15px;font-weight:600;color:#fff;text-decoration:none}
.foot-dot{position:absolute;top:4596px;width:28px;height:28px;border-radius:50%;border:2px solid #fff}
</style>
</head>
<body>

<div class="abs topbar">
  <span style="left:61px">Monday - Friday: 8:00 AM - 9:00 PM</span>
  <span style="left:330px">(509) 555-0182</span>
  <span style="left:600px">Monday - Friday: 8:00 AM - 9:00 PM</span>
  <span style="left:870px">(509) 555-0182</span>
  <i class="social-dot" style="left:990px"></i>
  <i class="social-dot" style="left:1031px"></i>
  <i class="social-dot" style="left:1072px"></i>
  <i class="social-dot" style="left:1113px"></i>
</div>

<header class="abs nav">
  <div class="brand"><i></i>Ridgecrest Balusters</div>
  <a style="left:382px">Home</a>
  <a style="left:476px">About Us</a>
  <a style="left:595px">Services</a>
  <a style="left:710px">Blog</a>
  <a style="left:789px">Gallery</a>
  <div class="btn-contact">Contact Us</div>
</header>

<section class="abs hero">
  <svg width="1200" height="820" viewBox="0 0 1200 820">
    <defs>
      <linearGradient id="heroPhoto" x1="0" y1="0" x2="1" y2="1">
        <stop offset="0" stop-color="#3c4650"/>
        <stop offset=".5" stop-color="#4b5a55"/>
        <stop offset="1" stop-color="#2e3335"/>
      </linearGradient>
      <linearGradient id="greenBand" x1="0" y1="0" x2="1" y2="0">
        <stop offset="0" stop-color="#063a1a"/>
        <stop offset="1" stop-color="#13843f"/>
      </linearGradient>
    </defs>
    <polygon role="img" aria-label="Photo of a deck with black aluminium glass railing overlooking a valley town" points="0,0 1200,0 1200,611 600,818 0,611" fill="url(#heroPhoto)"/>
    <polygon points="0,611 540,746 540,760 0,660" fill="url(#greenBand)"/>
    <polygon points="1200,611 663,746 663,760 1200,660" fill="url(#greenBand)"/>
    <polygon points="0,660 540,760 0,760" fill="#fff"/>
    <polygon points="1200,660 663,760 1200,760" fill="#fff"/>
  </svg>
</section>
<div class="abs hero-label">RIDGECREST BALUSTERS</div>
<h1 class="abs" style="left:61px;top:338px;width:760px;font-size:55px;line-height:68px;font-weight:800;color:#fff">THE PERFECT RAILING FOR EVERY PROJECT</h1>
<p class="abs hero-text">At Ridgecrest Balusters, We Believe That Every Outdoor Space Deserves The Perfect Blend Of Style, Safety, And Durability. Serving Homeowners, Builders, And Commercial Developers Across The Washington State.</p>
<div class="abs btn" style="left:61px;top:582px;width:137px;height:43px;font-size:14px">Learn More</div>

<section>
  <div class="ph" role="img" aria-label="Photo of a two-storey house with a dark deck and glass railing" style="left:65px;top:1003px;width:367px;height:367px;background:linear-gradient(160deg,#9aa3a8,#4c5256)"></div>
  <div class="ph" role="img" aria-label="Photo of an upper deck with glass panel railing" style="left:315px;top:1182px;width:267px;height:297px;background:linear-gradient(160deg,#8fa08a,#3e4446);outline:6px solid #fff"></div>
  <div class="abs badge"><span>25+</span><span>Year Experience</span></div>
  <h2 class="abs about-title">About Us</h2>
  <p class="abs about-sub">From Concept To Completion, We're With You Every Step</p>
  <p class="abs about-para">Transform Your Backyard Intropical Oasis With A Custom Swimming</p>
  <div class="check" style="top:1257px"><b><svg width="10" height="10" viewBox="0 0 10 10"><path d="M2 5l2 2 4-4" stroke="#fff" stroke-width="1.6" fill="none"/></svg></b>With Over 32,000 Pools Built Since 1994 In The Greater Tampa Area</div>
  <div class="check" style="top:1287px"><b><svg width="10" height="10" viewBox="0 0 10 10"><path d="M2 5l2 2 4-4" stroke="#fff" stroke-width="1.6" fill="none"/></svg></b>At Alder Pools, We Specialize In Creating Swimming Pools</div>
  <div class="check" style="top:1317px"><b><svg width="10" height="10" viewBox="0 0 10 10"><path d="M2 5l2 2 4-4" stroke="#fff" stroke-width="1.6" fill="none"/></svg></b>Alder Pools Is Committed To Building Pools That Fit Your Budget</div>
  <div class="abs btn" style="left:627px;top:1364px;width:137px;height:43px;font-size:14px">Learn More</div>
</section>

<section class="abs band" style="top:1558px;height:626px"></section>
<h2 class="abs sec-title" style="top:1596px;color:#fff">Services</h2>
<p class="abs sec-sub" style="top:1658px;color:#fff">Enhancing Homes And Businesses With Unique Designs</p>
<div class="svc" style="left:61px"><div class="ph" role="img" aria-label="Photo of black metal stair railing" style="background:linear-gradient(160deg,#e6e6e6,#8c8c8c)"></div><h3>Custom Railing<br>Solutions</h3><p>For A Sleek, Low-Maintenance Option, Our Powder-Coated Aluminum Railings.</p><div class="arrow"><svg width="36" height="20"><path d="M12 10h12M20 6l4 4-4 4" stroke="#fff" stroke-width="1.6" fill="none"/></svg></div></div>
<div class="svc" style="left:335px"><div class="ph" role="img" aria-label="Photo of exterior stair railing on a modern home" style="background:linear-gradient(160deg,#b8bcbc,#5a5f5f)"></div><h3>Railing Installation<br>Home</h3><p>For A Sleek, Low-Maintenance Option, Our Powder-Coated Aluminum Railings.</p><div class="arrow"><svg width="36" height="20"><path d="M12 10h12M20 6l4 4-4 4" stroke="#fff" stroke-width="1.6" fill="none"/></svg></div></div>
<div class="svc" style="left:609px"><div class="ph" role="img" aria-label="Photo of a patio with cable railing and chairs" style="background:linear-gradient(160deg,#8fb1d3,#3f5a78)"></div><h3>Cable Railing<br>Installation</h3><p>For A Sleek, Low-Maintenance Option, Our Powder-Coated Aluminum Railings.</p><div class="arrow"><svg width="36" height="20"><path d="M12 10h12M20 6l4 4-4 4" stroke="#fff" stroke-width="1.6" fill="none"/></svg></div></div>
<div class="svc" style="left:883px"><div class="ph" role="img" aria-label="Photo of glass railing held by standoff pins" style="background:linear-gradient(160deg,#a7d6cf,#2f6f68)"></div><h3>Glass Railing Stand<br>Off Pins</h3><p>For A Sleek, Low-Maintenance Option, Our Powder-Coated Aluminum Railings.</p><div class="arrow"><svg width="36" height="20"><path d="M12 10h12M20 6l4 4-4 4" stroke="#fff" stroke-width="1.6" fill="none"/></svg></div></div>
<div class="abs discover">Discover More</div>

<h2 class="abs sec-title" style="top:2252px;color:var(--ink)">Blog</h2>
<p class="abs sec-sub" style="top:2314px;color:var(--ink)">Creating Beautiful And Functional Spaces, One Post At A Time</p>
<article class="post" style="left:59px"><div class="ph" role="img" aria-label="Photo of a worker installing deck stair railing" style="background:linear-gradient(160deg,#7fa468,#3b4a33)"></div><h3>Custom Railing<br>Solutions</h3><p class="ex">For A Sleek, Low-Maintenance Option, Our Powder.</p><hr><div class="author"><i></i>Marla Hensley</div><p class="note">For A Sleek, Low-Maintenance Option, Our Powder.</p></article>
<article class="post" style="left:427px"><div class="ph" role="img" aria-label="Photo of glass stair railing on a deck" style="background:linear-gradient(160deg,#a8b8a2,#55605a)"></div><h3>Glass Railing Stand<br>Off Pins</h3><p class="ex">For A Sleek, Low-Maintenance Option, Our Powder.</p><hr><div class="author"><i></i>Marla Hensley</div><p class="note">For A Sleek, Low-Maintenance Option, Our Powder.</p></article>
<article class="post" style="left:793px"><div class="ph" role="img" aria-label="Photo of cable railing on a wooden deck" style="background:linear-gradient(160deg,#8fae7e,#8a6f55)"></div><h3>Cable Railing<br>Installation</h3><p class="ex">For A Sleek, Low-Maintenance Option, Our Powder.</p><hr><div class="author"><i></i>Marla Hensley</div><p class="note">For A Sleek, Low-Maintenance Option, Our Powder.</p></article>

<section class="abs band" style="top:2922px;height:705px"></section>
<h2 class="abs sec-title" style="top:2966px;color:#fff">Gallery</h2>
<p class="abs sec-sub" style="top:3029px;color:#fff">"Innovative Railings That Speak For Themselves</p>
<div class="ph" role="img" aria-label="Photo of a dark floating staircase" style="left:63px;top:3113px;width:281px;height:253px;background:linear-gradient(160deg,#6b5a4a,#151515)"></div>
<div class="ph" role="img" aria-label="Photo of black horizontal stair railing" style="left:63px;top:3378px;width:281px;height:159px;background:linear-gradient(160deg,#e2e2e2,#3a3a3a)"></div>
<div class="ph" role="img" aria-label="Photo of cable railing on a deck with flowers" style="left:360px;top:3113px;width:481px;height:206px;background:linear-gradient(160deg,#4f7a46,#9a9a96)"></div>
<div class="ph" role="img" aria-label="Photo of black post with cable railing close-up" style="left:360px;top:3330px;width:481px;height:207px;background:linear-gradient(160deg,#d6d6d4,#5a4630)"></div>
<div class="ph" role="img" aria-label="Photo of glass and steel stair railing over wood steps" style="left:858px;top:3113px;width:282px;height:253px;background:linear-gradient(160deg,#d7cbb8,#6b3a1e)"></div>
<div class="ph" role="img" aria-label="Photo of a spiral staircase with metal railing" style="left:858px;top:3378px;width:282px;height:159px;background:linear-gradient(160deg,#aebfcf,#2f3a44)"></div>
<div class="abs" style="left:61px;top:3567px;width:1079px;height:5px;background:#fff"></div>
<div class="abs" style="left:573px;top:3565px;width:36px;height:9px;background:var(--green-deep)"></div>

<h2 class="abs sec-title" style="top:3700px;color:var(--ink)">Contact Us</h2>
<p class="abs sec-sub" style="top:3758px;color:var(--ink)">Get In Touch With Us Today</p>
<div class="info-ic" style="top:3866px"><svg width="30" height="34" viewBox="0 0 30 34"><path d="M15 2a11 11 0 0 0-11 11c0 8 11 19 11 19s11-11 11-19A11 11 0 0 0 15 2z" fill="none" stroke="#fff" stroke-width="2.5"/><circle cx="15" cy="13" r="4" fill="#fff"/></svg></div>
<p class="info-h" style="top:3866px">Address</p>
<p class="info-t" style="top:3898px">2280 Cedar Bluff Rd. Yakima, Washington 98901</p>
<div class="info-ic" style="top:3972px"><svg width="32" height="32" viewBox="0 0 24 24"><path d="M6.6 10.8a15 15 0 0 0 6.6 6.6l2.2-2.2a1 1 0 0 1 1-.25 11.4 11.4 0 0 0 3.6.57 1 1 0 0 1 1 1V20a1 1 0 0 1-1 1A17 17 0 0 1 3 4a1 1 0 0 1 1-1h3.5a1 1 0 0 1 1 1c0 1.25.2 2.45.57 3.57a1 1 0 0 1-.25 1z" fill="#fff"/></svg></div>
<p class="info-h" style="top:3982px">Phone</p>
<p class="info-t" style="top:4016px">(509) 555-0146</p>
<div class="info-ic" style="top:4077px"><svg width="36" height="26" viewBox="0 0 36 26"><rect x="2" y="2" width="32" height="22" fill="none" stroke="#fff" stroke-width="2.5"/><path d="M2 2l16 13L34 2" fill="none" stroke="#fff" stroke-width="2.5"/></svg></div>
<p class="info-h" style="top:4088px">Email</p>
<p class="info-t" style="top:4122px">Hello@Ridgecrest.Example</p>
<div class="field" style="left:499px;top:3841px;width:305px;height:56px">First Name</div>
<div class="field" style="left:818px;top:3841px;width:306px;height:56px">Last Name</div>
<div class="field" style="left:499px;top:3913px;width:305px;height:56px">Phone Number</div>
<div class="field" style="left:818px;top:3913px;width:306px;height:56px">Email</div>
<div class="field" style="left:499px;top:3984px;width:625px;height:133px">Messages</div>
<div class="abs btn" style="left:499px;top:4139px;width:108px;height:41px;font-size:14px">Submit</div>

<footer class="footer">
  <svg class="abs" style="left:0;top:4255px" width="1200" height="389" viewBox="0 0 1200 389">
    <defs>
      <linearGradient id="footG" x1="0" y1="0" x2="0" y2="1">
        <stop offset="0" stop-color="#13843f"/>
        <stop offset="1" stop-color="#063a1a"/>
      </linearGradient>
    </defs>
    <polygon points="0,389 0,140 540,56 600,3 660,56 1200,140 1200,389" fill="url(#footG)"/>
  </svg>
  <div class="abs" style="left:0;top:4405px;width:1200px;text-align:center;color:#fff;font-size:32px;font-weight:700">Ridgecrest Balusters</div>
  <a style="left:367px">Home</a>
  <a style="left:460px">About Us</a>
  <a style="left:579px">Services</a>
  <a style="left:694px">Blog</a>
  <a style="left:775px">Gallery</a>
  <div class="abs" style="left:61px;top:4570px;width:1079px;height:1px;background:#fff"></div>
  <i class="foot-dot" style="left:62px"></i>
  <i class="foot-dot" style="left:116px"></i>
  <i class="foot-dot" style="left:170px"></i>
  <div class="abs" style="left:880px;top:4601px;width:260px;text-align:right;color:#fff;font-size:13px;text-decoration:underline">Copy Right @ All Right Received By</div>
</footer>

</body>
</html>
```